New signage for apartment community in the Pacific Northwest

Signage for an apartment community in the Pacific Northwest. It should have a contemporary northwest vibe with a fresh exciting feeling. We are open to the colors cayenne, white, charcoal and a splash of lime green. Sign to have the name 'VELTO' with the address number 28391 smaller underneath. sign can include a shape under the name or a feeling of energy in the shape of the name.

Target Market(s)

Young urban professionals

Industry/Entity Type

Real Estate Development

Requirements
Must have
• eyecatching
Should not have
• anything too cute or too busy

```html
<!DOCTYPE html>
<html lang="en">
<head>
<meta charset="utf-8">
<title>VELTO – Community Sign</title>
<link rel="stylesheet" href="https://fonts.googleapis.com/css2?family=Playfair+Display:wght@700&family=Montserrat:wght@500&display=swap">
<style>
  :root {
    --bg-dark: #3a3a3a;
    --bg-light: #7c7c7c;
    --wood-dark: #3e1d08;
    --wood-mid: #5a2d0f;
    --wood-light: #6e3a16;
    --trim-cream: #f4e6bb;
    --letter-white: #ffffff;
  }
  html, body {
    margin: 0;
    padding: 0;
    width: 796px;
    height: 1200px;
    overflow: hidden;
  }
  body {
    background: linear-gradient(135deg, var(--bg-dark) 0%, var(--bg-light) 100%);
  }
  .sign {
    display: block;
    width: 796px;
    height: 1200px;
  }
  .sign__name {
    font-family: "Playfair Display", Georgia, serif;
    font-weight: 700;
    font-size: 162px;
    fill: var(--letter-white);
  }
  .sign__address {
    font-family: "Montserrat", Arial, sans-serif;
    font-weight: 500;
    font-size: 16px;
    letter-spacing: 4px;
    fill: var(--letter-white);
  }
  .sign__rule {
    stroke: var(--letter-white);
    stroke-width: 1.2;
  }
  .sign__trim {
    fill: none;
    stroke: var(--trim-cream);
    stroke-width: 4;
  }
  .sign__ornament {
    fill: var(--trim-cream);
    opacity: 0.35;
  }
</style>
</head>
<body>
<svg class="sign" viewBox="0 0 796 1200" xmlns="http://www.w3.org/2000/svg">
  <defs>
    <linearGradient id="woodTone" x1="0" y1="0" x2="0" y2="1">
      <stop offset="0" stop-color="var(--wood-mid)"/>
      <stop offset="0.5" stop-color="var(--wood-light)"/>
      <stop offset="1" stop-color="var(--wood-dark)"/>
    </linearGradient>
    <filter id="signShadow" x="-10%" y="-10%" width="120%" height="130%">
      <feDropShadow dx="0" dy="8" stdDeviation="10" flood-color="#000" flood-opacity="0.45"/>
    </filter>
  </defs>

  <g class="sign__board" filter="url(#signShadow)">
    <path role="img" aria-label="Wood grain panel in warm browns"
      fill="url(#woodTone)"
      d="M76 447 H213 V396 H250 Q398 338 546 396 H583 V447 H720 Q748 447 748 475 V722 Q748 750 720 750 H583 V798 H546 Q398 872 250 798 H213 V750 H76 Q48 750 48 722 V475 Q48 447 76 447 Z"/>
  </g>

  <path class="sign__trim"
    d="M80 461 H227 V410 H258 Q398 356 538 410 H569 V461 H716 Q734 461 734 479 V718 Q734 736 716 736 H569 V784 H538 Q398 854 258 784 H227 V736 H80 Q62 736 62 718 V479 Q62 461 80 461 Z"/>

  <rect class="sign__ornament" role="img" aria-label="Decorative scroll flourish" x="296" y="442" width="204" height="36" rx="18"/>

  <text class="sign__name" x="398" y="643" text-anchor="middle">VELTO</text>

  <line class="sign__rule" x1="110" y1="694" x2="180" y2="694"/>
  <text class="sign__address" x="398" y="700" text-anchor="middle">28391, PACIFIC NORTHWEST</text>
  <line class="sign__rule" x1="616" y1="694" x2="686" y2="694"/>

  <rect class="sign__ornament" role="img" aria-label="Decorative scroll flourish" x="300" y="742" width="196" height="24" rx="12"/>
</svg>
</body>
</html>
```